Pediatric Occupational Therapy Brochure Design

This design really needs to stand out, especially with all the wordage that I have included. These brochures will be given to doctors, future clients, and caregivers. I have included the logo on by brochure, so incorporating the same or similar colors would be fantastic. A trifold brochure would probably be best to fit all the information, as this is a new business and needs to convey all the information in a way that people will read.

Target Market(s)

Doctor's offices and caregivers of children with disabilities.

Industry/Entity Type

Health Care

Font styles to use
Serif
Sans Serif

Colors
33a6d7
85acd3
ffffff
33b8a4
86cfc7

Requirements
Must have
• I would like the same colors of the logo incorporated in the brochure design.
Nice to have
• I would like to see the butterfly somehow in the background or used in the design. Also a trifold or two page design would be greatly appreciated as long as the information can fit.

```html
<!DOCTYPE html>
<html lang="en">
<head>
<meta charset="utf-8">
<title>Wren &amp; Willow Therapy – Pediatric Occupational Therapy Brochure</title>
<link rel="stylesheet" href="https://fonts.googleapis.com/css2?family=Maven+Pro:wght@400;500;600&family=Didact+Gothic&display=swap">
<style>
  :root{
    --teal-light:#80d0d1;
    --teal-pale:#a9e0e0;
    --teal-deep:#138a8c;
    --teal-ink:#0e7c80;
    --teal-head:#2aa3a5;
    --white:#ffffff;
    --ink:#1f2a2b;
    --photo-a:#cfe3ea;
    --photo-b:#e7c9a8;
  }
  *{box-sizing:border-box;margin:0;padding:0}
  html,body{width:1200px;height:928px;overflow:hidden;background:var(--white)}
  body{font-family:"Didact Gothic",sans-serif}
  .brochure{position:relative;width:1200px;height:928px;overflow:hidden}
  .panel{position:absolute;top:0;height:928px;width:400px;overflow:hidden}
  .panel--left{left:0;background:var(--teal-light)}
  .panel--middle{left:400px;background:var(--teal-light)}
  .panel--right{left:800px;background:var(--teal-light)}
  .panel-shapes{position:absolute;inset:0;width:400px;height:928px}

  h2,h3,.owner-name{font-family:"Maven Pro",sans-serif;font-weight:500}

  /* left panel */
  .brand{position:absolute;left:0;top:28px;width:210px;height:70px;background:var(--white);
    display:flex;align-items:center;gap:10px;padding-left:24px;
    font-family:"Maven Pro",sans-serif;font-weight:500;font-size:17px;color:var(--teal-deep)}
  .brand-dot{width:14px;height:14px;border-radius:50%;background:var(--teal-deep)}
  .owner-name{position:absolute;left:29px;top:108px;font-size:29px;line-height:35px;color:var(--white)}
  .owner-title{position:absolute;left:29px;top:182px;font-family:"Maven Pro",sans-serif;font-size:21px;color:var(--white)}
  .rule{border:0;border-top:2px dotted currentColor;position:absolute}
  .owner-rule{left:29px;top:213px;width:344px;color:var(--white)}
  .owner-bio{position:absolute;left:28px;top:226px;width:345px;color:var(--white);font-size:14px;line-height:21.3px;text-align:justify}
  .role-title{position:absolute;right:30px;top:604px;text-align:right;color:var(--teal-head);font-size:26px;line-height:30px}
  .role-rule{left:26px;top:700px;width:345px;color:var(--teal-head)}
  .role-body{position:absolute;left:28px;top:710px;width:345px;color:var(--ink);font-size:14px;line-height:21.3px;text-align:justify}

  /* middle panel */
  .photo{position:absolute}
  .photo--child{left:0;top:0;width:400px;height:332px;
    background:linear-gradient(135deg,var(--photo-a),#bfe6f0 45%,var(--photo-b));
    clip-path:polygon(0 0,100% 0,100% 100%,0 84%)}
  .services-title{position:absolute;left:23px;top:316px;color:var(--white);font-size:26px;line-height:31px}
  .services-rule{left:24px;top:383px;width:345px;color:var(--teal-deep)}
  .goals{position:absolute;left:24px;top:390px;width:347px;height:147px;background:var(--teal-deep);color:var(--white);padding:8px 22px}
  .goals h3{font-size:18px;margin-bottom:5px}
  .goals p{font-size:14px;line-height:21px}
  .checklist{list-style:none;position:absolute}
  .checklist li{position:relative;padding-left:22px;color:var(--teal-ink);font-size:16px;line-height:20px}
  .checklist li::before{content:"";position:absolute;left:3px;top:4px;border-left:10px solid transparent;border-bottom:10px solid var(--teal-deep)}
  .goal-list{left:22px;top:542px;width:360px}
  .goal-list li{margin-bottom:6.5px}

  /* right panel */
  .conditions-title{position:absolute;left:27px;top:24px;color:var(--white);font-size:26px;line-height:31px}
  .conditions-rule{left:27px;top:120px;width:346px;color:var(--white)}
  .condition-list{left:27px;top:134px;width:350px}
  .condition-list li{margin-bottom:6.7px}
  .photo--family{left:212px;top:588px;width:170px;height:170px;border-radius:50%;
    background:radial-gradient(circle at 40% 40%,#f3dcc8,#cfe9ee 70%);border:4px solid var(--white)}
  .involve-title{position:absolute;left:27px;top:655px;color:var(--white);font-size:24px;line-height:28px}
  .involve-rule{left:27px;top:713px;width:195px;color:var(--white)}
  .involve-body{position:absolute;left:27px;top:725px;width:346px;color:var(--white);font-size:14px;line-height:21.3px;text-align:justify}
  .involve-body p+p{margin-top:8px}
  .involve-body .short{width:200px;text-align:left}
</style>
</head>
<body>
<main class="brochure">

  <section class="panel panel--left">
    <svg class="panel-shapes" viewBox="0 0 400 928" aria-hidden="true">
      <polygon points="400,440 400,560 140,600" fill="#93d8d8"/>
      <polygon points="400,530 400,600 0,630" fill="#b6e5e5"/>
      <polygon points="0,632 400,598 400,928 0,928" fill="#ffffff"/>
    </svg>
    <div class="brand"><span class="brand-dot"></span>Wren &amp; Willow</div>
    <h1 class="owner-name">Marisol<br>Delgado</h1>
    <p class="owner-title">OTR, C/NDT | Owner</p>
    <hr class="rule owner-rule">
    <p class="owner-bio">My name is Marisol and I am a pediatric Occupational Therapist. I was born and raised in the Sunfield Valley and have provided services to the pediatric and adult population since 2012.<br>I am currently certified in Neuro-Developmental Treatment of Children with Cerebral Palsy and Other Neuromotor Disorders and have had the pleasure of working with children with various disorders and disabilities.<br>I am a dedicated OTR that works with each client and family to develop a specific plan of care to maximize functional ability across all environments.</p>
    <h2 class="role-title">Role of<br>Occupational Therapy<br>with Children</h2>
    <hr class="rule role-rule">
    <p class="role-body">Occupational therapists work with children, who have challenges, to fully participate in normal daily activities. Those challenges may be due to developmental delay, ADD/ADHD, autism, chromosomal differences, injury, trauma, and many others. An occupational therapist evaluates to assess areas of difficulty as well as strengths, and treat the child based on his or her specific needs.</p>
  </section>

  <section class="panel panel--middle">
    <div class="photo photo--child" role="img" aria-label="Photo of a young boy playing with modelling clay at a table"></div>
    <h2 class="services-title">Pediatric Occupational<br>Therapy Services</h2>
    <hr class="rule services-rule">
    <div class="goals">
      <h3>Occupational Therapy Goals</h3>
      <p>A child’s occupation is to be a kid!<br>Through the use of play, I can help<br>children acquire the skills needed<br>for the job of living.<br>These include, but are not limited to :</p>
    </div>
    <ul class="checklist goal-list">
      <li>Promoting independence in daily living skills- including dress, grooming, and feeding</li>
      <li>Facilitating developmental play skills</li>
      <li>Improving fine motor and eye-hand coordination skills</li>
      <li>Improving sensory processing skills such as organization, self-regulation and behavioral state</li>
      <li>Improving visual motor/visual perceptual skills including writing and coloring</li>
      <li>Addressing orthopedic complications and helping to increase function through the use of splinting and taping</li>
      <li>Improving balance and coordination skills through play</li>
    </ul>
  </section>

  <section class="panel panel--right">
    <svg class="panel-shapes" viewBox="0 0 400 928" aria-hidden="true">
      <polygon points="0,588 400,660 400,928 0,928" fill="#138a8c"/>
      <polygon points="0,588 260,635 0,640" fill="#5fb9b9"/>
    </svg>
    <h2 class="conditions-title">Conditions<br>that may benefit from<br>Occupational Therapy</h2>
    <hr class="rule conditions-rule">
    <ul class="checklist condition-list">
      <li>ADD/ADHD</li>
      <li>Auditory Processing Disorders</li>
      <li>Autism Spectrum Disorders</li>
      <li>Cancer/Leukemia</li>
      <li>Cerebral Palsy</li>
      <li>Congenital Heart Disease</li>
      <li>Developmental Delay</li>
      <li>Failure to Thrive</li>
      <li>Genetic Disorders/Birth Defects</li>
      <li>Hemophilia</li>
      <li>Neurological Disorders</li>
      <li>Orthopedic injuries or Surgery</li>
      <li>Sensory Integration Disorders</li>
      <li>Trauma Brain Injuries</li>
      <li>Tracheostomy and/or ventilator dependency</li>
      <li>and any condition that affects a child’s growth and development</li>
    </ul>
    <div class="photo photo--family" role="img" aria-label="Photo of a mother playing with her baby and toy blocks"></div>
    <h2 class="involve-title">Parental<br>Involvement:</h2>
    <hr class="rule involve-rule">
    <div class="involve-body">
      <p><span class="short" style="display:block">Each child’s success is strongly dependent upon the</span>caregiver’s involvement. Therapy does not stop when the session ends and must be carried over across all environments in a child’s life.</p>
      <p>I specialize in working with parents and caregivers to ensure home programs are in place to make each child’s progress the best.</p>
    </div>
  </section>

</main>
</body>
</html>
```